Book cover needed for Christian Non-Fiction Book

I need book cover design (eBook , Paperback, and possibly case laminate Hardcover) for use on PQL and Halvet Print.
Title: Go Forth Called
Sub-Title: Leaving Shelter and Walking in Faithful Purpose
Author: Owen Callery
Also on front cover "Forward by R. Lisel Marrow"

I like clean/simple designs. Below are links to examples of covers I like...
https://www.bookvantle.example/dp/X4821QPT7M?tag=plumwick-20&linkCode=ogi&th=1&psc=1
https://www.bookvantle.example/dp/X49KTRMWHZ?tag=plumwick-20&linkCode=ogi&th=1&psc=1
https://www.bookvantle.example/dp/X22HQC51NT?tag=plumwick-20&linkCode=ogi&th=1&psc=1
https://www.bookvantle.example/dp/X48F3WZPDR?tag=plumwick-20&linkCode=ogi&th=1&psc=1
https://www.bookvantle.example/dp/X4M7UVVCLE?tag=plumwick-20&linkCode=ogi&th=1&psc=1
https://www.bookvantle.example/dp/X2R9HNNKA6?tag=plumwick-20&linkCode=ogi&th=1&psc=1

The main idea for Go Forth Called is that God is a sending God and being "on the move" or journeying is central to God's character, and therefore God's people. I write about our hesitancy to "go," and how the Bible is full of stories about people "going" from Abraham to Jesus, to the disciples of Jesus.

The core biblical text is the Great Commission in Matthew 28:16-20, where Jesus sends out his followers, though some of them doubt.

This paragraph from the forward by R. Lisel Marrow captures the tone of the book well:
This book is a call amid the turmoil. Sacred scripture contains no shortage of narratives in which humans are pulled from their ordinary lives with an inciting incident whose stakes are high. These Biblical figures are lulled from complacency and comfort zones—and yet they are reluctant to serve because they question their ability and influence. Their lessons are relevant for us today: They, and we, are always called and sent with authority. The power of the Holy Spirit equips their “going”—and ours. It’s a sending out that looks less like mastery and more humility. It’s a sending out that is unequivocal service to others modelled in a rabbi-reformer who washed feet and touched the unclean.

I have previously published two shorter books and would be very interested in getting new covers for the old books these so that the three have a similar feel. Whichever designer I go with for "Go Forth Called" I would also want to work with on creating a "branded look" for the other two books.

Target Market(s)

Christian, Religion, Spirituality Readers

Requirements
Must have
• The front cover must have this copy...
Go Forth Called
Leaving Shelter and Walking in Faithful Purpose
Owen Callery
Forward by R. Lisel Marrow

Must be willing to do the full paperback and/or hardcover, but start with thefront cover please
Nice to have
• See attached files for some book covers I like

```html
<!DOCTYPE html>
<html lang="en">
<head>
<meta charset="utf-8">
<title>Go Forth Called — Owen Callery</title>
<link rel="stylesheet" href="https://fonts.googleapis.com/css2?family=Montserrat:wght@400;500&family=Nunito:wght@900&display=swap">
<style>
  :root {
    --kraft: #b5a789;
    --kraft-light: #c2b597;
    --kraft-dark: #a6977a;
    --ink-light: #ffffff;
    --title-shadow: rgba(60, 48, 28, 0.55);
    --plane-tone: #a8997b;
    --plane-light: #cbbf9f;
  }
  html, body {
    margin: 0;
    padding: 0;
    overflow: hidden;
  }
  .cover {
    position: relative;
    width: 849px;
    height: 1200px;
    overflow: hidden;
    background:
      radial-gradient(ellipse at 30% 25%, var(--kraft-light) 0%, transparent 60%),
      radial-gradient(ellipse at 80% 85%, var(--kraft-dark) 0%, transparent 55%),
      var(--kraft);
    font-family: "Montserrat", Arial, sans-serif;
    color: var(--ink-light);
  }
  .subtitle {
    position: absolute;
    left: 58px;
    top: 30px;
    margin: 0;
    font-weight: 500;
    font-size: 31px;
    line-height: 1.22;
    letter-spacing: 0.3px;
  }
  .title {
    position: absolute;
    left: 0;
    width: 100%;
    top: 508px;
    margin: 0;
    text-align: center;
    font-family: "Nunito", "Arial Rounded MT Bold", sans-serif;
    font-weight: 900;
    font-size: 96px;
    letter-spacing: 1px;
    text-transform: uppercase;
    line-height: 1;
    text-shadow:
      0 0 6px var(--title-shadow),
      0 0 18px var(--title-shadow),
      0 0 30px rgba(60, 48, 28, 0.35);
  }
  .plane-art {
    position: absolute;
    left: 205px;
    top: 605px;
    width: 565px;
    height: 330px;
  }
  .author {
    position: absolute;
    left: 0;
    width: 100%;
    top: 1020px;
    margin: 0;
    text-align: center;
    font-size: 33px;
    font-weight: 400;
    letter-spacing: 0.5px;
  }
  .foreword {
    position: absolute;
    left: 0;
    width: 100%;
    top: 1066px;
    margin: 0;
    text-align: center;
    font-size: 33px;
    font-weight: 400;
    letter-spacing: 0.5px;
  }
</style>
</head>
<body>
  <main class="cover">
    <p class="subtitle">Leaving Shelter<br>and Walking in Faithful Purpose</p>
    <h1 class="title">Go Forth Called</h1>
    <svg class="plane-art" viewBox="0 0 565 330" role="img" aria-label="Paper airplane illustration gliding upward to the right, in muted kraft tones">
      <defs>
        <radialGradient id="planeGlow" cx="60%" cy="40%" r="60%">
          <stop offset="0%" stop-color="var(--plane-light)" stop-opacity="0.55"/>
          <stop offset="100%" stop-color="var(--plane-tone)" stop-opacity="0"/>
        </radialGradient>
      </defs>
      <rect x="0" y="0" width="565" height="330" fill="url(#planeGlow)"/>
    </svg>
    <p class="author">Owen Callery</p>
    <p class="foreword">Forward by R. Lisel Marrow</p>
  </main>
</body>
</html>
```